Harbor Nightclub

Nightclub flyer., digital single sided, for KV and PX. I included samples of some previous flyers we've used. Sample Info:
HARBOR
FRIDAYS
FRI MAY 1 2020
DJ VORTAN (club floor)
DJ RUZO & DJ TAV (residents on the lounge floor)
4217 Marlow Avenue Sacramento
www.harborvenuehall.example for list/VIP inquiries

Target Market(s)

Upscale top 40 crowd but want some cool and artsy like the examples included.

Font styles to use
Sans Serif

Requirements
Must have
• Harbor Logo
Nice to have
• Would be nice if the flyer can be incorporated later with DJ photos (sometimes we will add dj photos to pixagram etc). Would like a big city type of feel.
Should not have
• Nothing too sexual.

```html
<!DOCTYPE html>
<html lang="en">
<head>
<meta charset="utf-8">
<title>Harbor Fridays</title>
<link rel="stylesheet" href="https://fonts.googleapis.com/css2?family=Inter:wght@200;300;400;700&family=Roboto+Condensed:wght@300;400&display=swap">
<style>
  :root {
    --night: #1b0b3b;
    --night-deep: #140830;
    --white: #ffffff;
    --orchid: #c45fb4;
    --neon-pink: #ff4fe0;
    --neon-cyan: #3fd8ec;
    --glow: #ff9cf5;
  }
  * { margin: 0; padding: 0; box-sizing: border-box; }
  html, body { width: 961px; height: 1200px; overflow: hidden; background: var(--night-deep); }
  .flyer {
    position: relative;
    width: 961px;
    height: 1200px;
    overflow: hidden;
    background: radial-gradient(ellipse 520px 460px at 460px 520px, #3a1466 0%, var(--night) 60%, var(--night-deep) 100%);
    color: var(--white);
    font-family: "Inter", Arial, sans-serif;
    text-align: center;
  }
  .headliner {
    position: absolute; top: 56px; left: 0; width: 100%;
    font-weight: 700; font-size: 23px; letter-spacing: 0.5px;
  }
  .residents {
    position: absolute; top: 86px; left: 0; width: 100%;
    font-weight: 400; font-size: 50px; color: var(--orchid); letter-spacing: 0.5px;
  }
  .neon-frame { position: absolute; top: 0; left: 0; width: 961px; height: 1200px; }
  .illustration {
    position: absolute; left: 30px; top: 190px; width: 760px; height: 560px;
    border-radius: 46% 40% 44% 50%;
    background:
      radial-gradient(ellipse 200px 230px at 470px 300px, rgba(255,210,90,0.75) 0%, rgba(230,60,200,0.55) 55%, rgba(230,60,200,0) 100%),
      radial-gradient(ellipse 220px 150px at 200px 170px, rgba(160,80,200,0.7) 0%, rgba(160,80,200,0) 100%);
  }
  .flare {
    position: absolute; left: 330px; top: 650px; width: 260px; height: 220px;
    background: radial-gradient(ellipse at center, rgba(255,255,255,0.95) 0%, var(--glow) 18%, rgba(220,70,220,0.35) 45%, rgba(220,70,220,0) 75%);
  }
  .night-title {
    position: absolute; top: 735px; left: 0; width: 100%;
    font-weight: 200; font-size: 190px; line-height: 1; letter-spacing: 2px;
  }
  .event-date {
    position: absolute; top: 920px; left: 0; width: 100%;
    font-weight: 700; font-size: 40px; word-spacing: 8px;
  }
  .venue-mark {
    position: absolute; top: 1025px; left: 50%; width: 50px; height: 50px; margin-left: -25px;
    border-radius: 50%; background: var(--white);
  }
  .venue-name {
    position: absolute; top: 1090px; left: 0; width: 100%;
    font-weight: 400; font-size: 28px; letter-spacing: 1px;
  }
  .venue-details {
    position: absolute; left: 0; width: 100%;
    font-family: "Roboto Condensed", Arial, sans-serif; font-weight: 300; font-size: 20px;
  }
  .venue-address { top: 1128px; }
  .venue-web { top: 1155px; }
</style>
</head>
<body>
<main class="flyer">
  <p class="headliner">DJ VORTAN</p>
  <p class="residents">DJ RUZO &amp; DJ TAV</p>

  <svg class="neon-frame" viewBox="0 0 961 1200" aria-hidden="true">
    <polygon points="116,219 882,167 494,781" fill="none" stroke="var(--neon-cyan)" stroke-width="3"/>
    <polygon points="175,177 899,193 450,761" fill="none" stroke="var(--neon-pink)" stroke-width="8" opacity="0.35"/>
    <polygon points="175,177 899,193 450,761" fill="none" stroke="#ffc6f6" stroke-width="3"/>
  </svg>

  <div class="illustration" role="img" aria-label="Illustration of an astronaut in a yellow and magenta suit carrying a boombox and making a peace sign"></div>
  <div class="flare" aria-hidden="true"></div>

  <h1 class="night-title">FRIDAYS</h1>
  <p class="event-date">MAY 1 2020</p>

  <div class="venue-mark" aria-hidden="true"></div>
  <p class="venue-name">HARBOR</p>
  <p class="venue-details venue-address">4217 MARLOW AVENUE SACRAMENTO</p>
  <p class="venue-details venue-web">WWW.HARBORVENUEHALL.EXAMPLE FOR LIST/VIP INQUIRIES</p>
</main>
</body>
</html>
```